earthmoving and roadworks company looking for a fresh and updated logo to help us stand out

We are looking for a business card design for our earthmoving, demolition and road works company named Wombridge Hire. We cover a broad range of work so our business card needs to be flexible to suit all of the different services we provide. We have a few different bits of machinery including several water trucks for transporting water and spraying the roads, an excavator (digger) for earthmoving, a tipper truck that carries grain/soil and other items, a skidmule and two rollers. our business card needs to be simple but effective and bold. Our colour palette is yellow, black and white and I have attached a copy of our logo but please note our logo is only the 'Wombridge hire' bit with attached circle, the 'watercarts, rollers, cartage' below are not part of the logo. Please feel free to modify the logo to better suit the business card. The design must be easy to read and to the point. It should make us look reliable and professional.

Target Market(s)

Wide range of clients including government sectors and private individuals

Industry/Entity Type

Construction

Contact Information for Business Card

We need a business card that is bold and straight to the point but with easy to read information and an eye catching design. We are open to either a single sided or double sided design

Colors
fbee3d
fcf5b5
fbf289
fbed22

Requirements
Must have
• The business card must include
• our logo
• our contact details as listed below:
• Dwayne Ostler
• Managing Director
• 02 6911 5033
• 0477 301 926
• wombridgehire@tallnetmail.com
Nice to have
• Nice to have a picture of machinery or part of machinery in the business card design. We would also like to incorporate our business activities which are: demolition, earthmoving, road works and cartage. It would also be highly desirable if it included a list of our machinery: Watercarts, Rollers, Excavator, Skidmule, Truck & Dog. we are open to the possibility of either single sided or double sided designs
Should not have
• should not have too many colours or detract from the main information. should not be too busy.

```html
<!DOCTYPE html>
<html lang="en">
<head>
<meta charset="utf-8">
<title>Wombridge Hire – Business Card</title>
<link rel="stylesheet" href="https://fonts.googleapis.com/css2?family=Open+Sans:wght@400;600;700&display=swap">
<style>
  :root {
    --card-black: #0d0d0d;
    --brand-yellow: #fbed22;
    --brand-yellow-soft: #fbf289;
    --ink-white: #ffffff;
    --ink-grey: #bfbfbf;
    --page-bg: #e9e7e2;
  }
  html, body {
    margin: 0;
    width: 1200px;
    height: 913px;
    overflow: hidden;
    background: var(--page-bg);
    font-family: "Open Sans", Arial, sans-serif;
  }
  .sheet {
    width: 1200px;
    height: 913px;
    display: flex;
    align-items: center;
    justify-content: center;
    gap: 50px;
  }
  .card {
    width: 540px;
    height: 310px;
    border-radius: 16px;
    overflow: hidden;
    background: var(--card-black);
    box-shadow: 0 10px 28px rgba(0,0,0,.25);
  }
  .card svg { display: block; }
  .brand-name { font-family: "Open Sans", Arial, sans-serif; font-weight: 700; fill: var(--ink-white); }
  .person-name { font-family: "Open Sans", Arial, sans-serif; font-weight: 700; fill: var(--ink-white); font-size: 23px; }
  .person-role { font-family: "Open Sans", Arial, sans-serif; font-weight: 600; fill: var(--brand-yellow); font-size: 14px; }
  .contact-line { font-family: "Open Sans", Arial, sans-serif; font-weight: 400; fill: var(--ink-white); font-size: 14px; }
  .services { font-family: "Open Sans", Arial, sans-serif; font-weight: 600; fill: var(--card-black); font-size: 14px; }
  .fleet { font-family: "Open Sans", Arial, sans-serif; font-weight: 600; fill: var(--ink-white); font-size: 14px; }
  .icon { fill: none; stroke: var(--brand-yellow); stroke-width: 1.6; }
</style>
</head>
<body>
<main class="sheet">

  <!-- Front: contact side -->
  <section class="card card--front" aria-label="Business card front">
    <svg width="540" height="310" viewBox="0 0 540 310">
      <path id="front-curve" d="M0,300 Q300,300 540,200" fill="none"/>
      <path class="swoosh-edge" d="M0,289 Q300,289 540,187 L540,200 Q300,300 0,300 Z" fill="var(--ink-grey)"/>
      <path class="swoosh" d="M0,300 Q300,300 540,200 L540,310 L0,310 Z" fill="var(--brand-yellow)"/>

      <g class="brand-lockup">
        <circle cx="42" cy="190" r="14" fill="var(--brand-yellow)"/>
        <text class="brand-name" x="64" y="197" font-size="21">Wombridge Hire</text>
      </g>

      <line class="divider" x1="262" y1="60" x2="262" y2="178" stroke="var(--brand-yellow)" stroke-width="1.2"/>

      <text class="person-name" x="276" y="76">Dwayne Ostler</text>
      <text class="person-role" x="276" y="98">Managing Director</text>

      <g class="contact">
        <path class="icon" d="M277,120 q0,10 9,12 l2,-3 -3,-3 -2,1 q-3,-2 -3,-5 l1,-2 -3,-3 z"/>
        <text class="contact-line" x="296" y="131">02 6911 5033</text>
        <rect class="icon" x="279" y="141" width="8" height="12" rx="1.5"/>
        <text class="contact-line" x="296" y="153">0477 301 926</text>
        <rect class="icon" x="277" y="164" width="12" height="9"/>
        <path class="icon" d="M277,164 l6,5 6,-5"/>
        <text class="contact-line" x="296" y="174">wombridgehire@tallnetmail.com</text>
      </g>

      <text class="services" dy="16">
        <textPath href="#front-curve" startOffset="130">Demolition, Earthmoving, Road Works And Cartage</textPath>
      </text>
    </svg>
  </section>

  <!-- Back: brand side -->
  <section class="card card--back" aria-label="Business card back">
    <svg width="540" height="310" viewBox="0 0 540 310">
      <path id="back-curve" d="M0,300 Q330,300 540,170" fill="none"/>
      <path class="swoosh" d="M0,300 Q330,300 540,170 L540,310 L0,310 Z" fill="var(--brand-yellow)"/>

      <g class="brand-lockup">
        <circle cx="110" cy="125" r="22" fill="var(--brand-yellow)"/>
        <text class="brand-name" x="144" y="137" font-size="34">Wombridge Hire</text>
      </g>

      <text class="fleet" dy="-10">
        <textPath href="#back-curve" startOffset="100">Watercarts-Rollers-Excavator-Skidmule-Truck&amp; Dog</textPath>
      </text>
    </svg>
  </section>

</main>
</body>
</html>
```